Need modern simple design for magazine ad, apartment and condo roofer.

I need a half page magazine ad for a local roofer to publish in an industry magazine. Apartment associations industry. All types of roofs. Shingle and Flat
Need the design to be creative and modern, clean and simple. I do not want a busy design. One that stands out and makes a point quickly.
Logo must be prominent.
DO NOT USE PHOTOS FROM MY WEBSITE PLEASE. Looking for something new.
I work on entire complexes not houses.

Need to make sure our phone number and email address are listed at the bottom. Here is my website www.vorbelan.com
Want to stay away from standard clip arts of tools, homes, apartment buildings.
Half Horizontal 7.25 x 4.75
Ads should be in PDF and JPG format.

Target Market(s)

Apartment or Condo owners looking for large scale roofing projects

Industry/Entity Type

Roofing

Requirements
Must have
• Prominent Logo
Simple Clean Design
Create graphics
Not Busy
Should not have
• Clip Art
No Photos from my website

```html
<!DOCTYPE html>
<html lang="en">
<head>
<meta charset="utf-8">
<title>Vorbelan Multifamily Roofing – Half Page Ad</title>
<link href="https://fonts.googleapis.com/css2?family=Lato:wght@400;700;900&display=swap" rel="stylesheet">
<style>
  :root {
    --stage: #b9bcbf;
    --tile-glow: #5fb4f5;
    --tile-light: #2f8ae6;
    --tile-mid: #0b5cc2;
    --tile-deep: #073a86;
    --tile-shadow: #06173a;
    --night: #03060c;
    --brand-blue: #2f8fe0;
    --ink-white: #ffffff;
  }
  * { margin: 0; padding: 0; box-sizing: border-box; }
  html, body {
    width: 1200px;
    height: 848px;
    overflow: hidden;
    background: var(--stage);
  }
  .ad {
    position: absolute;
    left: 101px;
    top: 98px;
    width: 999px;
    height: 654px;
    overflow: hidden;
    font-family: "Lato", sans-serif;
    color: var(--ink-white);
  }
  .ad__backdrop {
    position: absolute;
    inset: 0;
    background:
      radial-gradient(ellipse 45% 22% at 62% 42%, rgba(120,195,255,0.35), transparent 70%),
      radial-gradient(ellipse 35% 18% at 28% 28%, rgba(120,195,255,0.35), transparent 70%),
      radial-gradient(ellipse 30% 12% at 75% 15%, rgba(150,210,255,0.3), transparent 70%),
      linear-gradient(172deg, rgba(6,23,58,0.55) 0%, transparent 18%, transparent 30%, rgba(6,23,58,0.45) 36%, transparent 44%, transparent 100%),
      linear-gradient(180deg, var(--tile-light) 0%, var(--tile-mid) 45%, var(--tile-deep) 72%, var(--tile-shadow) 86%, var(--night) 100%);
  }
  .ad__content {
    position: absolute;
    left: 237px;
    top: 250px;
    width: 550px;
  }
  .brand {
    display: flex;
    align-items: center;
    justify-content: center;
    gap: 20px;
    height: 160px;
  }
  .brand__mark {
    width: 52px;
    height: 52px;
    background: var(--brand-blue);
    flex: none;
  }
  .brand__name {
    font-weight: 900;
    font-size: 46px;
    line-height: 1.08;
    color: var(--ink-white);
  }
  .contact {
    margin-top: 11px;
    border-top: 1px solid var(--ink-white);
    padding-top: 7px;
    display: flex;
    justify-content: space-between;
    font-size: 17px;
    font-weight: 700;
    letter-spacing: 0.4px;
    color: var(--ink-white);
  }
  .contact__divider { font-weight: 400; color: var(--ink-white); }
</style>
</head>
<body>
  <main class="ad">
    <div class="ad__backdrop" role="img" aria-label="Close-up photograph of glossy blue curved roof tiles fading into darkness at the bottom"></div>
    <div class="ad__content">
      <div class="brand">
        <span class="brand__mark"></span>
        <span class="brand__name">Vorbelan<br>Multifamily Roofing</span>
      </div>
      <p class="contact">
        <span class="contact__item">817.555.0142</span>
        <span class="contact__divider">|</span>
        <span class="contact__item">info@vorbelan.com</span>
        <span class="contact__divider">|</span>
        <span class="contact__item">www.vorbelan.com</span>
      </p>
    </div>
  </main>
</body>
</html>
```